Certificate of Completion - Educational Trainings

We are looking for a certificate of completion for individuals who complete one of our specific trainings. Files should be provided in a Word (docx) or PowerPoint (pptx) format. The "Talmoray example.png" file is to show necessary information. Copies of logos have been included for design purposes.

Target Market(s)

Training Participants

Industry/Entity Type

Healthcare

Font styles to use
Sans Serif

```html
<!DOCTYPE html>
<html lang="en">
<head>
<meta charset="utf-8">
<title>Talmoray Certificate of Completion</title>
<link href="https://fonts.googleapis.com/css2?family=Jost:wght@400;500;600&family=Montserrat:wght@700&family=Kaushan+Script&display=swap" rel="stylesheet">
<style>
  :root {
    --page-bg: #e9e9e7;
    --paper: #f8f8f6;
    --ink: #151515;
    --green-dark: #1f7a2c;
    --green: #3f9b3a;
    --green-light: #7cc05a;
  }
  * { margin: 0; padding: 0; box-sizing: border-box; }
  html, body { width: 1200px; height: 1054px; overflow: hidden; background: var(--page-bg); }
  .certificate {
    position: absolute; left: 50px; top: 102px; width: 1100px; height: 850px;
    background: var(--paper); box-shadow: 0 4px 18px rgba(0,0,0,.12);
    font-family: 'Jost', sans-serif; color: var(--ink);
  }
  .leaf-band {
    position: absolute; inset: 18px;
    background: linear-gradient(135deg, var(--green-light), var(--green), var(--green-light), var(--green));
  }
  .leaf-band-inner { position: absolute; inset: 30px; background: var(--paper); }
  .frame {
    position: absolute; inset: 64px;
    border: 2px solid var(--green);
    outline: 1px solid var(--green); outline-offset: 5px;
  }
  .content { position: absolute; inset: 0; text-align: center; }
  .brand {
    position: absolute; top: 98px; left: 0; right: 0;
    display: flex; justify-content: center; align-items: center; gap: 12px;
    font-family: 'Montserrat', sans-serif; font-weight: 700; font-size: 27px; letter-spacing: 2px;
  }
  .brand-dot { width: 22px; height: 22px; border-radius: 50%; background: var(--green-dark); }
  .title {
    position: absolute; top: 132px; left: 0; right: 0;
    font-weight: 400; font-size: 112px; letter-spacing: 4px; line-height: 1;
  }
  .subtitle {
    position: absolute; top: 246px; left: 0; right: 0;
    font-family: 'Kaushan Script', cursive; font-size: 52px; line-height: 1;
  }
  .awarded {
    position: absolute; top: 322px; left: 0; right: 0;
    font-size: 19px; letter-spacing: 1px; text-transform: uppercase;
  }
  .recipient {
    position: absolute; top: 350px; left: 250px; right: 250px;
    font-family: 'Kaushan Script', cursive; font-size: 62px; color: var(--green-dark);
    line-height: 1.2; border-bottom: 1.5px solid var(--green); padding-bottom: 4px;
  }
  .details {
    position: absolute; top: 448px; left: 0; right: 0;
    font-size: 17px; line-height: 1.25;
  }
  .divider {
    position: absolute; top: 574px; left: 330px; right: 330px;
    display: flex; align-items: center; gap: 14px;
  }
  .divider-line { flex: 1; height: 1.5px; background: var(--green); }
  .divider-dot { width: 12px; height: 12px; border-radius: 50%; background: var(--green-dark); }
  .address {
    position: absolute; top: 596px; left: 0; right: 0;
    font-size: 12px; line-height: 1.3; text-transform: uppercase; letter-spacing: .5px;
  }
  .accordance {
    position: absolute; top: 660px; left: 0; right: 0;
    font-size: 12px; line-height: 1.3; text-transform: uppercase; letter-spacing: .5px;
  }
  .field-block { position: absolute; width: 170px; text-align: center; }
  .field-value { font-size: 12px; padding-bottom: 4px; border-bottom: 1.5px solid var(--green); }
  .field-value.signature { font-family: 'Kaushan Script', cursive; font-size: 14px; }
  .field-label { font-size: 12px; text-transform: uppercase; letter-spacing: .5px; margin-top: 4px; }
  .date-block { left: 150px; top: 712px; }
  .signature-block { right: 150px; top: 520px; }
</style>
</head>
<body>
  <main class="certificate">
    <div class="leaf-band" role="img" aria-label="Decorative green leaf border pattern"><div class="leaf-band-inner"></div></div>
    <div class="frame"></div>
    <div class="content">
      <div class="brand"><span class="brand-dot"></span><span>TALMORAY</span></div>
      <h1 class="title">CERTIFICATE</h1>
      <p class="subtitle">Of Completion</p>
      <p class="awarded">This Certificate ID Awarded To</p>
      <p class="recipient">Marcus Hollerin</p>
      <div class="details">
        <p>For Successful Completion Of</p>
        <p>Best Practices : Budget Process/Budget Building</p>
        <p>Completed Online</p>
        <p>Field Of Study Finance</p>
        <p>CPE Credits: 1</p>
      </div>
      <div class="divider"><span class="divider-line"></span><span class="divider-dot"></span><span class="divider-line"></span></div>
      <div class="address">
        <p>48 Harbor Lane, Ste. 310</p>
        <p>Brenford, ME 04090</p>
        <p>Credit Council Sponsor Number 70318</p>
      </div>
      <div class="accordance">
        <p>In accordance with the standard of the Continuing Credit Council.</p>
        <p>CPE credits have been granted based on a 50 minute hour.</p>
      </div>
      <div class="field-block date-block">
        <p class="field-value">03/21/2025</p>
        <p class="field-label">Completion Date</p>
      </div>
      <div class="field-block signature-block">
        <p class="field-value signature">Clara Denvik</p>
        <p class="field-label">Completion Date</p>
      </div>
    </div>
  </main>
</body>
</html>
```